VORKEL COMPOSITES INC website in USA

VORKEL COMPOSITES INC incorporated and operated in USA needs a completely new design of website. This Wyoming based company is a importer and distributor of composites material to supply mainly to American and Canadian/Mexican customers. Our main products includes Carbon Fiber, Aramid Fiber, Glass Fiber, Basalt Fiber, High Silica Glass, Quartz Fiber, S-Glass, Alumina Fiber, Vacuum Auxiliary.

We are one stop composites solution provider for Automotive, Aerospace, Construction, Electrical and Machinery industries.

We are exclusive sales company in North America for Doraq Composites produced from China and their other Asia facilities.

Target Market(s)

USA and Canada

Industry/Entity Type

Composites materials

Coding

Coded - Design and coding required

Number of Pages Required

5+ page

Requirements
Nice to have
• Color theme to match our corporate logo VORKEL. VORKEL stands for Vantor Omniline Reliant Kinetic Export Lodge

```html
<!DOCTYPE html>
<html lang="en">
<head>
<meta charset="utf-8">
<title>VORKEL Composites Inc</title>
<link href="https://fonts.googleapis.com/css2?family=Questrial&display=swap" rel="stylesheet">
<style>
:root{
  --dark:#2c2623;
  --orange:#e5832b;
  --light:#efede9;
  --white:#ffffff;
  --text:#3a3533;
  --muted:#5c5653;
  --border:#dcd8d4;
}
*{margin:0;padding:0;box-sizing:border-box}
html,body{width:1200px;height:5059px;overflow:hidden}
body{font-family:"Questrial",Arial,sans-serif;color:var(--text);background:var(--white);position:relative}
section,header,footer{position:absolute;left:0;width:1200px}
.abs{position:absolute}
.label{color:var(--orange);font-size:16px;letter-spacing:.5px;text-transform:uppercase}
.heading{font-size:20px;letter-spacing:.6px;text-transform:uppercase;line-height:38px}
.body-text{font-size:14px;line-height:34px}
.btn{position:absolute;display:flex;align-items:center;justify-content:center;gap:10px;height:40px;border-radius:20px;font-size:12px;letter-spacing:.6px;text-transform:uppercase}
.btn svg{width:11px;height:11px}
.btn-orange{background:var(--orange);color:var(--white)}
.btn-white{background:var(--white);color:var(--orange)}
.btn-outline{border:1.5px solid var(--white);color:var(--orange)}
.photo{position:absolute}

/* logo */
.logo{display:flex;align-items:center;gap:12px;color:var(--white)}
.logo-mark{width:14px;height:14px;background:var(--orange);border-radius:50%}
.logo-name{font-size:30px;letter-spacing:1px}
.logo-rule{width:1px;height:38px;background:rgba(255,255,255,.6)}
.logo-tag{font-size:8px;line-height:11px;width:96px;color:#ddd}

/* hero */
.hero{top:0;height:503px;background:var(--dark);overflow:hidden}
.hero-photo{left:560px;top:0;width:640px;height:503px;clip-path:polygon(28% 0,100% 0,100% 100%,0 100%);background:linear-gradient(150deg,#8d9096 0%,#4c4f55 40%,#1f2024 75%,#3a3c40 100%)}
.nav{position:absolute;left:492px;top:42px;display:flex;gap:21px;font-size:11.5px;color:var(--white);letter-spacing:.2px}
.nav .active{color:var(--orange)}
.hero h1{position:absolute;left:103px;top:155px;font-weight:400;font-size:28px;color:var(--white);letter-spacing:.6px}
.hero h1 span{color:var(--orange)}
.hero h2{position:absolute;left:103px;top:206px;font-weight:400;font-size:23px;color:var(--white);letter-spacing:.6px}
.hero p{position:absolute;left:103px;top:258px;width:520px;font-size:14.5px;line-height:34px;color:var(--white)}

/* quote */
.quote{top:503px;height:218px;background:var(--orange)}
.quote h2{position:absolute;top:42px;width:100%;text-align:center;font-weight:400;font-size:25px;color:var(--white);letter-spacing:.6px}
.field{position:absolute;top:118px;width:230px;height:44px;border:1.5px solid var(--white);border-radius:22px;color:var(--white);font-size:12px;padding-left:22px;display:flex;align-items:center;text-transform:uppercase}

/* about */
.about{top:721px;height:721px}
.about-shade{left:0;top:0;width:463px;height:477px;background:var(--light)}
.about-photo{left:158px;top:85px;width:399px;height:550px;background:linear-gradient(135deg,#8e9094 0%,#3a3b3f 45%,#151517 80%,#2a2b2e 100%)}
.about-text{left:633px;top:80px;width:480px}

/* impact */
.impact{top:1442px;height:286px;background:var(--dark)}
.impact-orange{left:437px;top:0;width:763px;height:286px;background:var(--orange)}
.stat{position:absolute;top:48px;color:var(--white)}
.stat svg{width:58px;height:58px}
.stat-num{font-size:34px;margin-top:16px}
.stat-label{font-size:13px;line-height:34px;margin-top:6px;text-transform:uppercase}

/* industries */
.industries{top:1728px;height:660px;background:var(--dark);color:var(--white)}
.ind-photo{left:0;top:92px;width:553px;height:482px;background:linear-gradient(120deg,#b7bcc2 0%,#8a8f96 35%,#c46b2c 55%,#d88a4a 70%,#7d8289 100%)}
.ind-text{left:622px;top:90px;width:470px}
.ind-item{display:flex;align-items:center;gap:14px;color:var(--orange);font-size:13.5px;margin-top:22px;text-transform:uppercase}
.ind-item svg{width:20px;height:20px}

/* products */
.products{top:2388px;height:1151px}
.center{position:absolute;width:100%;text-align:center}
.card{position:absolute;width:307px;height:376px;border:1.5px solid var(--border);border-radius:10px;overflow:hidden;text-align:center;background:var(--white)}
.card-photo{height:187px}
.card h3{font-weight:400;font-size:17px;color:var(--orange);margin-top:32px;letter-spacing:.4px}
.card p{font-size:13.5px;line-height:34px;margin:10px 22px 0;color:var(--text)}
.card.featured{background:var(--orange);border-color:var(--orange)}
.card.featured h3,.card.featured p{color:var(--white)}

/* testimonials */
.testimonials{top:3539px;height:513px;background:var(--light)}
.t-card{position:absolute;top:162px;height:277px;background:var(--white);border-radius:12px}
.t-quote{position:absolute;left:-28px;top:36px;width:40px;height:40px;background:var(--orange);border-radius:6px;display:flex;align-items:center;justify-content:center}
.t-stars{position:absolute;left:82px;top:34px;display:flex;gap:5px}
.t-stars svg{width:14px;height:14px}
.t-body{position:absolute;left:82px;top:66px;width:330px;font-size:14px;line-height:34px}
.t-name{position:absolute;left:82px;top:222px;font-size:12.5px;text-transform:uppercase}
.t-name span{color:var(--orange)}
.arrow-btn{position:absolute;top:3838px;width:28px;height:28px;border:1.5px solid var(--text);border-radius:50%;display:flex;align-items:center;justify-content:center}

/* partner */
.partner{top:4052px;height:717px}
.partner-shade{left:692px;top:0;width:508px;height:525px;background:var(--light)}
.partner-photo{left:596px;top:85px;width:491px;height:548px;background:linear-gradient(140deg,#c4c5c7 0%,#7b7d80 35%,#3a3b3e 70%,#1d1d1f 100%)}
.partner-text{left:112px;top:90px;width:430px}
.partner-logo{position:absolute;left:112px;top:638px;display:flex;align-items:center;gap:10px;font-size:26px;color:var(--dark)}
.partner-logo i{width:20px;height:20px;background:#6cbf2a;display:block}

/* footer */
.footer{top:4769px;height:290px;background:var(--dark);color:var(--white)}
.footer .logo{position:absolute;left:462px;top:64px}
.foot-nav{position:absolute;top:172px;width:100%;display:flex;justify-content:center;gap:16px;font-size:12.5px;text-transform:uppercase}
.copy{position:absolute;top:221px;width:100%;text-align:center;font-size:12.5px;text-transform:uppercase}
</style>
</head>
<body>

<header class="hero">
  <div class="photo hero-photo" role="img" aria-label="Close-up of woven carbon fiber surface with jet engines behind"></div>
  <div class="logo abs" style="left:110px;top:28px">
    <span class="logo-mark"></span><span class="logo-name">VORKEL</span>
    <span class="logo-rule"></span>
    <span class="logo-tag">Vantor Omniline Reliant Kinetic Export Lodge</span>
  </div>
  <nav class="nav">
    <span class="active">HOME</span><span>ABOUT US</span><span>PRODUCTS</span><span>INDUSTRIES SERVED</span><span>DORAQ PARTNERSHIP</span><span>RESOURCES</span>
  </nav>
  <h1>ADVANCED <span>COMPOSITE MATERIALS</span></h1>
  <h2>FOR THE FUTURE OF ENGINEERING</h2>
  <p>Supplying high-performance fibers and composite solutions across North America.</p>
  <a class="btn btn-white" style="left:103px;top:362px;width:184px">VIEW PRODUCTS <svg viewBox="0 0 12 12"><path d="M2 10L10 2M4 2h6v6" stroke="currentColor" fill="none" stroke-width="1.5"/></svg></a>
  <a class="btn btn-outline" style="left:307px;top:362px;width:164px">GET A QUOTE <svg viewBox="0 0 12 12"><path d="M2 10L10 2M4 2h6v6" stroke="currentColor" fill="none" stroke-width="1.5"/></svg></a>
</header>

<section class="quote">
  <h2>REQUEST A QUOTE</h2>
  <div class="field" style="left:111px">Name</div>
  <div class="field" style="left:361px">Email</div>
  <div class="field" style="left:610px;justify-content:space-between;padding-right:22px">Products <svg width="9" height="6" viewBox="0 0 9 6"><path d="M0 0h9L4.5 6z" fill="#fff"/></svg></div>
  <a class="btn btn-white" style="left:859px;top:118px;width:230px;height:44px;border-radius:22px">REQUEST A QUOTE <svg viewBox="0 0 12 12"><path d="M2 10L10 2M4 2h6v6" stroke="currentColor" fill="none" stroke-width="1.5"/></svg></a>
</section>

<section class="about">
  <div class="abs about-shade"></div>
  <div class="photo about-photo" role="img" aria-label="Curved sheet of black woven carbon fiber"></div>
  <div class="abs about-text">
    <div class="label">About Us</div>
    <div class="heading" style="margin-top:22px">Your trusted partner for<br>high-performance fibers and materials</div>
    <p class="body-text" style="margin-top:14px">VORKEL Composites Inc. (Vantor Omniline Reliant Kinetic Export Lodge), based in Wyoming, USA, is a leading importer and distributor of high-performance composite materials. We provide innovative fiber solutions to customers across the United States, Canada, and Mexico, serving industries such as automotive, aerospace, construction, electrical, and machinery.</p>
    <p class="body-text" style="margin-top:10px">At VORKEL, we combine global sourcing, industry knowledge, and local commitment to provide a one-stop composite solution for all your material needs.</p>
  </div>
  <a class="btn btn-orange" style="left:633px;top:592px;width:158px">LEARN MORE <svg viewBox="0 0 12 12"><path d="M2 10L10 2M4 2h6v6" stroke="currentColor" fill="none" stroke-width="1.5"/></svg></a>
</section>

<section class="impact">
  <div class="abs impact-orange"></div>
  <div class="abs" style="left:110px;top:56px">
    <div class="label">Our Impact</div>
    <div class="heading" style="color:var(--white);margin-top:24px;line-height:41px">Driving innovation and<br>excellence across<br>industries</div>
  </div>
  <div class="stat" style="left:510px">
    <svg viewBox="0 0 58 58" fill="none" stroke="#fff" stroke-width="1.6"><circle cx="17" cy="10" r="5"/><circle cx="29" cy="7" r="5"/><circle cx="41" cy="10" r="5"/><path d="M8 26c0-6 4-9 9-9M50 26c0-6-4-9-9-9M20 20c2-3 5-5 9-5s7 2 9 5"/><path d="M6 34l10-6 8 4 6-3 12 8M52 34l-10-6M16 42l8 6 6-2 8 4 10-8M6 34l6 10M52 34l-6 10"/></svg>
    <div class="stat-num">500+</div>
    <div class="stat-label">Satisfied clients<br>across North America</div>
  </div>
  <div class="stat" style="left:818px">
    <svg viewBox="0 0 58 58" fill="none" stroke="#fff" stroke-width="1.6"><circle cx="29" cy="26" r="20"/><circle cx="29" cy="22" r="6"/><path d="M17 40c2-7 7-10 12-10s10 3 12 10"/><path d="M29 2l2 4 4 .5-3 3 1 4-4-2-4 2 1-4-3-3 4-.5z M10 10l1.5 3 3 .4-2 2 .5 3-3-1.5-3 1.5.5-3-2-2 3-.4z M48 10l1.5 3 3 .4-2 2 .5 3-3-1.5-3 1.5.5-3-2-2 3-.4z"/></svg>
    <div class="stat-num">10+</div>
    <div class="stat-label">Years of experience in composite<br>material distribution</div>
  </div>
</section>

<section class="industries">
  <div class="photo ind-photo" role="img" aria-label="Bundled orange and gray cables in an industrial rack"></div>
  <div class="abs ind-text">
    <div class="label">Industries We Serve</div>
    <div class="heading" style="margin-top:22px">Serving industries that drive<br>innovation</div>
    <div class="ind-item"><svg viewBox="0 0 20 20" fill="none" stroke="#e5832b" stroke-width="1.8"><circle cx="10" cy="10" r="8"/><circle cx="10" cy="10" r="2"/><path d="M2.5 8h15M10 12v6"/></svg>Automotive</div>
    <p class="body-text" style="margin-top:8px">Lightweight, high-strength composites that enhance performance, fuel efficiency, and safety in vehicles.</p>
    <div class="ind-item"><svg viewBox="0 0 20 20" fill="#e5832b"><path d="M18 2c-1-1-3 0-4 1l-3 3-8-2-2 2 6 4-3 3-3-.5L0 13l4 1.5L5.5 18l1-1-.5-3 3-3 4 6 2-2-2-8 3-3c1-1 2-3 1-4z"/></svg>Aerospace</div>
    <p class="body-text" style="margin-top:8px">Advanced fibers engineered to meet stringent standards for strength, durability, and reliability in aviation and space applications.</p>
  </div>
  <a class="btn btn-orange" style="left:622px;top:530px;width:252px">EXPLORE OUR INDUSTRIES <svg viewBox="0 0 12 12"><path d="M2 10L10 2M4 2h6v6" stroke="currentColor" fill="none" stroke-width="1.5"/></svg></a>
</section>

<section class="products">
  <div class="center label" style="top:80px">Our Products</div>
  <div class="center heading" style="top:118px">Our High-Performance Fiber Solutions</div>

  <div class="card" style="left:111px;top:196px">
    <div class="card-photo" role="img" aria-label="Carbon fiber sheets on a factory line" style="background:linear-gradient(160deg,#6d7a8f,#2a2d33 60%,#9ca3ad)"></div>
    <h3>CARBON FIBER</h3><p>Lightweight, strong, and versatile – ideal for high-performance structural applications.</p>
  </div>
  <div class="card featured" style="left:446px;top:196px">
    <div class="card-photo" role="img" aria-label="Dark woven aramid fabric" style="background:linear-gradient(160deg,#3a3a3c,#121213)"></div>
    <h3>ARAMID FIBER</h3><p>Exceptional strength and impact resistance for protective and industrial applications.</p>
  </div>
  <div class="card" style="left:781px;top:196px">
    <div class="card-photo" role="img" aria-label="Glowing blue glass fiber strands" style="background:radial-gradient(circle at 45% 50%,#bfe2ff,#2b6fd1 35%,#0c1a3a 75%)"></div>
    <h3>GLASS FIBER</h3><p>Durable and cost-effective solutions for construction, insulation, and engineering projects.</p>
  </div>
  <div class="card" style="left:111px;top:610px">
    <div class="card-photo" role="img" aria-label="Black basalt fiber rolls" style="background:linear-gradient(160deg,#e4e4e4,#8a8a8a 50%,#1a1a1a)"></div>
    <h3>BASALT FIBER</h3><p>Eco-friendly, high-temperature resistant fibers for construction and industrial use.</p>
  </div>
  <div class="card" style="left:446px;top:610px">
    <div class="card-photo" role="img" aria-label="Coiled blue glowing silica glass fiber" style="background:radial-gradient(ellipse at 50% 55%,#6fb4ff,#1f4fc4 40%,#06102b 80%)"></div>
    <h3>HIGH SILICA GLASS</h3><p>Heat-resistant fibers for aerospace, electronics, and industrial applications.</p>
  </div>
  <div class="card" style="left:781px;top:610px">
    <div class="card-photo" role="img" aria-label="Quartz wafer diagram on dark background" style="background:radial-gradient(circle at 50% 50%,#9aa3b0,#3b4250 35%,#111318 70%)"></div>
    <h3>QUARTZ FIBER</h3><p>Superior thermal stability for precision applications in high temperature environments.</p>
  </div>

  <a class="btn btn-orange" style="left:508px;top:1024px;width:184px">VIEW PRODUCTS <svg viewBox="0 0 12 12"><path d="M2 10L10 2M4 2h6v6" stroke="currentColor" fill="none" stroke-width="1.5"/></svg></a>
</section>

<section class="testimonials">
  <div class="center label" style="top:48px">Testimonials</div>
  <div class="center heading" style="top:86px">What Our Clients Say</div>

  <div class="t-card" style="left:137px;width:426px">
    <div class="t-quote"><svg width="22" height="18" viewBox="0 0 22 18" fill="#fff"><path d="M0 18V9C0 4 3 1 8 0v3C5 4 4 6 4 9h5v9zM13 18V9c0-5 3-8 8-9v3c-3 1-4 3-4 6h5v9z"/></svg></div>
    <div class="t-stars"><svg viewBox="0 0 14 14"><path d="M7 0l2 5h5l-4 3 1.5 5L7 10l-4.5 3L4 8 0 5h5z" fill="#e5832b"/></svg><svg viewBox="0 0 14 14"><path d="M7 0l2 5h5l-4 3 1.5 5L7 10l-4.5 3L4 8 0 5h5z" fill="#e5832b"/></svg><svg viewBox="0 0 14 14"><path d="M7 0l2 5h5l-4 3 1.5 5L7 10l-4.5 3L4 8 0 5h5z" fill="#e5832b"/></svg><svg viewBox="0 0 14 14"><path d="M7 0l2 5h5l-4 3 1.5 5L7 10l-4.5 3L4 8 0 5h5z" fill="#e5832b"/></svg><svg viewBox="0 0 14 14"><path d="M7 0l2 5h5l-4 3 1.5 5L7 10l-4.5 3L4 8 0 5h5z" fill="#e5832b"/></svg></div>
    <p class="t-body">"Vorkel's carbon fiber products helped us reduce vehicle weight while maintaining structural integrity. Their team is responsive and truly understands our needs."</p>
    <div class="t-name"><span>Dana Whitfield,</span> Product Manager</div>
  </div>
  <div class="t-card" style="left:657px;width:429px">
    <div class="t-quote"><svg width="22" height="18" viewBox="0 0 22 18" fill="#fff"><path d="M0 18V9C0 4 3 1 8 0v3C5 4 4 6 4 9h5v9zM13 18V9c0-5 3-8 8-9v3c-3 1-4 3-4 6h5v9z"/></svg></div>
    <div class="t-stars"><svg viewBox="0 0 14 14"><path d="M7 0l2 5h5l-4 3 1.5 5L7 10l-4.5 3L4 8 0 5h5z" fill="#e5832b"/></svg><svg viewBox="0 0 14 14"><path d="M7 0l2 5h5l-4 3 1.5 5L7 10l-4.5 3L4 8 0 5h5z" fill="#e5832b"/></svg><svg viewBox="0 0 14 14"><path d="M7 0l2 5h5l-4 3 1.5 5L7 10l-4.5 3L4 8 0 5h5z" fill="#e5832b"/></svg><svg viewBox="0 0 14 14"><path d="M7 0l2 5h5l-4 3 1.5 5L7 10l-4.5 3L4 8 0 5h5z" fill="#e5832b"/></svg><svg viewBox="0 0 14 14"><path d="M7 0l2 5h5l-4 3 1.5 5L7 10l-4.5 3L4 8 0 5h5z" fill="#e5832b"/></svg></div>
    <p class="t-body">"Working with Vorkel was seamless. Their S-Glass and high-silica fibers met our rigorous standards, and delivery was always on time."</p>
    <div class="t-name"><span>Mara Olsen,</span> Engineering Lead</div>
  </div>
</section>
<div class="arrow-btn" style="left:46px"><svg width="10" height="10" viewBox="0 0 10 10"><path d="M6.5 1.5L3 5l3.5 3.5" stroke="#3a3533" fill="none" stroke-width="1.5"/></svg></div>
<div class="arrow-btn" style="left:1124px"><svg width="10" height="10" viewBox="0 0 10 10"><path d="M3.5 1.5L7 5 3.5 8.5" stroke="#3a3533" fill="none" stroke-width="1.5"/></svg></div>

<section class="partner">
  <div class="abs partner-shade"></div>
  <div class="photo partner-photo" role="img" aria-label="Draped woven composite fabric in soft light"></div>
  <div class="abs partner-text">
    <div class="label">Our Partner</div>
    <div class="heading" style="margin-top:22px">About Doraq-Composite</div>
    <p class="body-text" style="margin-top:14px">Welcome to Doraq Composites, your premier destination for top-quality composites and exceptional service. Our company has been providing high-quality composites to customers for many years, and we take great pride in our ability to consistently deliver excellence in both product quality and customer service.</p>
    <p class="body-text" style="margin-top:10px">At Doraq Composites, we specialize in the design, development, and manufacture of advanced composites for a wide range of industries, including aerospace, automotive, marine, and construction.</p>
  </div>
  <div class="partner-logo"><i></i>DORAQ</div>
</section>

<footer class="footer">
  <div class="logo">
    <span class="logo-mark"></span><span class="logo-name">VORKEL</span>
    <span class="logo-rule"></span>
    <span class="logo-tag">Vantor Omniline Reliant Kinetic Export Lodge</span>
  </div>
  <nav class="foot-nav">
    <span>Home</span><span>|</span><span>About Us</span><span>|</span><span>Products</span><span>|</span><span>Industries Served</span><span>|</span><span>Resources</span><span>|</span><span>Contact Us</span>
  </nav>
  <div class="copy">© 2025 VORKEL Composite Inc. All rights reserved.</div>
</footer>

</body>
</html>
```